Homepage Website Design for luxury picnic company

We need a homepage designed for a luxury picnic business to match our updated branding/logo which we're currently completing on ArtHivePro with another competition. Please see attached logo/colour example to use for now.

PLEASE NOTE: We are only after graphic design concepts as part of this competition. I will get another developer to actually code the website.

It is important that this website is very elegant/luxurious and stands out from a visual perspective. The images really need to match the content/sections also. The new branding colours are silver with a dark background. Please create the new website homepage to match these colours/branding.

Please create as many concepts as possible and then I will provide feedback from there

The website content including sections is here https://papers.quillnest.net/doc/7hRtK2mWqPz9LbXv4nYcJ8eFgTs3uAd6Vk1oNwEiQy/view?mode=shared

Images to use are located here https://vault.boxmerile.net/store/folders/8KmWpT3r-ZxQa5Hn92VbLcYeRduf?mode=shared and there is also lots of videos at this link which you can screenshot images out of if needed https://www.filetrunko.net/sh/k728vrum3wdx2h/QQTrfm7LkWn5EaZ9J4hvdPcXy?get=0

Any questions please contact me

```html
<!DOCTYPE html>
<html lang="en">
<head>
<meta charset="utf-8">
<title>Ridgeview Picnics — Home</title>
<link rel="stylesheet" href="https://fonts.googleapis.com/css2?family=Bebas+Neue&family=Outfit:wght@300;400;500;600&family=Roboto+Condensed:wght@400&display=swap">
<style>
  :root {
    --page-bg: #f3f3f3;
    --ink: #1c1c1e;
    --ink-soft: #6a6a6e;
    --ink-mid: #222226;
    --night: #0b0e18;
    --sky-top: #4b4f5c;
    --sky-mid: #2a3140;
    --ridge: #0d1016;
    --silver-light: #f4f4f4;
    --silver-mid: #b9b9b9;
    --silver-dark: #8e8e8e;
    --edge: #a9a9a9;
    --badge: #1aa6d6;
    --card: #ffffff;
  }
  * { box-sizing: border-box; margin: 0; padding: 0; }
  html, body { width: 1183px; height: 1200px; overflow: hidden; }
  body {
    position: relative;
    background: var(--page-bg);
    font-family: "Outfit", sans-serif;
    color: var(--ink);
  }

  /* Hero */
  .hero { position: absolute; inset: 0 0 auto 0; height: 600px; }
  .hero-scene { position: absolute; left: 0; top: 0; width: 1183px; height: 560px; }
  .brand {
    position: absolute; left: 41px; top: 6px; width: 106px; height: 167px;
    background: var(--night);
    display: flex; align-items: center; justify-content: center; gap: 5px;
  }
  .brand-dot { width: 6px; height: 6px; border-radius: 50%; background: var(--silver-mid); }
  .brand-name {
    font-family: "Outfit", sans-serif; font-weight: 500; font-size: 13px;
    color: var(--silver-light); line-height: 1.1; text-align: left;
  }
  .safety-badge {
    position: absolute; left: 1101px; top: 16px; width: 40px; height: 40px;
    border-radius: 50%; background: var(--badge); border: 2px solid #fff;
  }
  .hero-title {
    position: absolute; left: 0; width: 1100px; top: 194px; text-align: center;
    font-family: "Bebas Neue", sans-serif; font-size: 54px; letter-spacing: 1.5px; line-height: 1;
    background: linear-gradient(90deg, #fff 0%, #fff 38%, #9a9a9a 48%, #fff 56%, #fff 100%);
    -webkit-background-clip: text; background-clip: text; color: transparent;
  }
  .hero-tagline {
    position: absolute; left: 0; width: 1100px; top: 260px; text-align: center;
    font-weight: 400; font-size: 18px; letter-spacing: 4.6px; color: #e9e9e9;
  }
  .hero-cta {
    position: absolute; left: 468px; top: 330px; width: 183px; height: 45px;
    border: 2px solid #fff; border-radius: 8px;
    background: linear-gradient(90deg, var(--silver-dark), var(--silver-light) 25%, var(--silver-mid) 55%, #e6e6e6 80%, var(--silver-dark));
    font-family: "Roboto Condensed", sans-serif; font-size: 17px; color: var(--ink);
    display: flex; align-items: center; justify-content: center;
    box-shadow: 0 2px 6px rgba(0,0,0,.4);
  }
  .hero-couple {
    position: absolute; left: 948px; top: 132px; width: 150px; height: 442px;
    border-radius: 60px 60px 14px 14px;
    background: linear-gradient(180deg, #2b3a33 0%, #3d4a44 40%, #4d5f9a 62%, #1f2124 100%);
    filter: drop-shadow(0 8px 6px rgba(0,0,0,.35));
  }

  /* Services */
  .services-heading {
    position: absolute; left: 149px; top: 620px;
    font-size: 28px; font-weight: 500; letter-spacing: 2.2px; color: var(--ink);
  }
  .services-rule {
    position: absolute; left: 152px; top: 661px; width: 43px; height: 7px;
    background: linear-gradient(180deg, #d7d7d7, #8f8f8f);
    border-left: 3px solid var(--ink); border-right: 3px solid var(--ink);
  }
  .service-card {
    position: absolute; top: 701px; width: 274px; height: 240px;
    background: var(--card); border-radius: 7px;
    box-shadow: 0 10px 18px rgba(0,0,0,.16);
    padding: 25px 20px 0 24px;
  }
  .service-card.bliss { left: 149px; }
  .service-card.unwind {
    left: 448px;
    background: radial-gradient(ellipse at 30% 85%, #c8c8c8 0%, transparent 45%),
                radial-gradient(ellipse at 85% 15%, #c9c9c9 0%, transparent 40%),
                linear-gradient(135deg, #eeeeee, #dcdcdc 55%, #e9e9e9);
  }
  .service-card.indulge { left: 746px; }
  .service-title {
    font-size: 15.5px; font-weight: 600; letter-spacing: 2px; color: var(--ink);
    line-height: 20px;
  }
  .service-text {
    margin-top: 13px; font-size: 10.7px; font-weight: 400; letter-spacing: 1px;
    line-height: 19.7px; color: var(--ink-soft); white-space: nowrap;
  }
  .unwind .service-text { color: var(--ink-mid); }
  .service-text strong { font-weight: 600; color: var(--ink); }
</style>
</head>
<body>
  <header class="hero">
    <svg class="hero-scene" viewBox="0 0 1183 560" role="img" aria-label="Dusk photograph of cloudy sky over forested mountain ridges">
      <defs>
        <linearGradient id="sky" x1="0" y1="0" x2="0" y2="1">
          <stop offset="0" stop-color="#4b4f5c"/>
          <stop offset="0.22" stop-color="#3a3f4c"/>
          <stop offset="0.42" stop-color="#2a3140"/>
          <stop offset="0.62" stop-color="#141822"/>
          <stop offset="1" stop-color="#0d1016"/>
        </linearGradient>
      </defs>
      <path d="M0 0 H1183 V497 Q591 590 0 497 Z" fill="url(#sky)"/>
      <path d="M0 497 Q591 590 1183 497" fill="none" stroke="#a9a9a9" stroke-width="3"/>
    </svg>

    <div class="brand"><span class="brand-dot"></span><span class="brand-name">Ridgeview<br>Picnics</span></div>
    <div class="safety-badge" aria-hidden="true"></div>

    <h1 class="hero-title">Share an unforgettable moment</h1>
    <p class="hero-tagline">Luxury picnics at breathtaking locations</p>
    <a class="hero-cta">BOOK YOUR PICNIC</a>

    <div class="hero-couple" role="img" aria-label="Couple embracing while looking out over the valley"></div>
  </header>

  <main>
    <h2 class="services-heading">Our Services</h2>
    <div class="services-rule"></div>

    <article class="service-card bliss">
      <h3 class="service-title">BLISS</h3>
      <p class="service-text">We enable you to enjoy true quality<br>time with your partner, friends or<br>family. We do this by creating the per-<br>fect atmosphere to celebrate a special<br>moment in your life or to simply spoil<br>yourself!</p>
    </article>

    <article class="service-card unwind">
      <h3 class="service-title">UNWIND</h3>
      <p class="service-text">Let us do everything for you so you can<br>enjoy a stress free experience. You will<br>also discover the Blue Mountains like<br>you never have before! Each of our<br>picnic spots are absolutely stunning<br>and also very private.</p>
    </article>

    <article class="service-card indulge">
      <h3 class="service-title">INDULGE</h3>
      <p class="service-text">Our delicious picnics will have your<br>mouth watering! You can design your<br>own picnic by choosing from our exten-<br>sive menu along with 2 choices of your<br>favourite alcoholic &amp; non-alcoholic<br>beverages. We cater for all dietary<br>requirements and also have a <strong>BYO</strong><br>option</p>
    </article>
  </main>
</body>
</html>
```